Mental Health & Addiction Podcast Art

Project: Podcast Cover Art / Visual Identity
Podcast Name: The Mending Path
Focus: Recovery from substance use and mental health
Objectives
Create compelling podcast artwork that:
Reflects the themes of hope, healing, and personal growth
Establishes credibility and professionalism
Appeals to individuals seeking recovery resources and support
Maintains strong brand consistency with Larkspur Wellness
Brand Integration Requirements
Logo incorporation: Integrate an element from the Larkspur Wellness Logo—potentially an abstract or partial use of the sun motif
Flexibility: Open to creative interpretations (e.g., sun rays as background texture, sunrise gradient, partial sun as a design accent)
Mandatory: Must adhere to existing Larkspur Wellness brand guidelines (approved color palette, typography, and visual style)

Target Market(s)

United states, people with addiction and mental health disorders.

Industry/Entity Type

Wellness

Font styles to use
Other font styles liked:
• See Brand Guide

Requirements
Must have
• Match brand guide, in corporate elements of the Larkspur Wellness Logo icon

```html
<!DOCTYPE html>
<html lang="en">
<head>
<meta charset="utf-8">
<title>The Mending Path — Podcast Cover</title>
<link rel="stylesheet" href="https://fonts.googleapis.com/css2?family=Montserrat:wght@500&family=Noto+Serif:wght@700;800&family=Poppins:wght@500&display=swap">
<style>
  :root {
    --sky-deep: #0b4460;
    --sky-mid: #7c8f7e;
    --sky-warm: #d8ad6a;
    --sky-orange: #f6a640;
    --sun-core: #fffbe4;
    --hill-teal: #06708f;
    --hill-light: #5b9cb4;
    --hill-deep: #044660;
    --path-gold: #a88a4c;
    --brand-orange: #f5a800;
    --brand-teal: #03708f;
    --brand-navy: #064560;
    --white: #ffffff;
  }
  * { margin: 0; padding: 0; box-sizing: border-box; }
  html, body {
    width: 1200px;
    height: 1200px;
    overflow: hidden;
    background: var(--sky-deep);
  }
  .cover {
    position: relative;
    width: 1200px;
    height: 1200px;
    overflow: hidden;
  }
  .cover__scene {
    position: absolute;
    inset: 0;
    background:
      radial-gradient(ellipse 330px 300px at 608px 640px, rgba(255,253,230,1) 0%, rgba(255,246,190,0.85) 30%, rgba(255,230,140,0.35) 60%, rgba(255,220,120,0) 100%),
      linear-gradient(180deg, transparent 0%, transparent 66%, rgba(91,156,180,0.9) 74%, var(--hill-teal) 84%, var(--hill-deep) 100%),
      linear-gradient(180deg, var(--sky-deep) 0%, #3f6d74 15%, var(--sky-mid) 28%, var(--sky-warm) 48%, var(--sky-orange) 68%, var(--sky-orange) 100%);
  }
  .brand {
    position: absolute;
    top: 72px;
    left: 0;
    width: 100%;
    display: flex;
    justify-content: center;
    align-items: center;
    gap: 14px;
  }
  .brand__mark {
    width: 70px;
    height: 70px;
    border: 3px solid var(--white);
    border-radius: 50%;
  }
  .brand__name {
    font-family: "Montserrat", sans-serif;
    font-weight: 500;
    font-size: 43px;
    letter-spacing: -0.5px;
    color: var(--white);
  }
  .title {
    position: absolute;
    top: 216px;
    left: 0;
    width: 100%;
    text-align: center;
    font-family: "Noto Serif", serif;
    line-height: 1;
  }
  .title__line { display: block; }
  .title__the {
    font-weight: 700;
    font-size: 142px;
    color: var(--brand-orange);
    letter-spacing: -4px;
  }
  .title__mending {
    margin-top: 14px;
    font-weight: 700;
    font-size: 144px;
    color: var(--brand-teal);
    letter-spacing: -4px;
  }
  .title__path {
    margin-top: 14px;
    font-weight: 800;
    font-size: 146px;
    color: var(--brand-navy);
    letter-spacing: -4px;
  }
  .label {
    position: absolute;
    top: 1100px;
    left: 0;
    width: 100%;
    text-align: center;
    font-family: "Poppins", sans-serif;
    font-weight: 500;
    font-size: 44px;
    letter-spacing: 22px;
    padding-left: 22px;
    color: var(--white);
  }
</style>
</head>
<body>
  <main class="cover">
    <div class="cover__scene" role="img" aria-label="Illustrated sunrise glowing over rolling teal hills, with a golden winding path leading toward the sun"></div>

    <header class="brand">
      <span class="brand__mark"></span>
      <span class="brand__name">LARKSPUR WELLNESS</span>
    </header>

    <h1 class="title">
      <span class="title__line title__the">THE</span>
      <span class="title__line title__mending">MENDING</span>
      <span class="title__line title__path">PATH</span>
    </h1>

    <p class="label">Podcast</p>
  </main>
</body>
</html>
```